VoltNest EV Charger Installation

We are an electrical contractor "Brannock Electric" http://brannockelectricservices.example.

New site is for a division we are creating. http://voltnestelectric.example/ is registered on Google domains.
Company is registered as VoltNest LLC.
VoltNest is something we are trying out to see if we can find a niche installing EV chargers and EV Charger outlets in existing homes and businesses. Looking to work it as a division off from Brannock Electric short term and if successful it would become a stand alone business. Often times this requires additional work to meet code. Work such as adding smoke & carbon monoxide detectors, new electrical panels and upgrading the electrical Main Service Meter system.
Will need to coordinate this site with our current Brannock Electric website. Not sure how this can work. We like the look of our current Brannock Electric Wordpress site, but it is dated and broken, in need of a rebuild or repair as well.
Need a website as a landing point for Google Maps inquiries and possibly as a way to drive customers to call for our services. Need to be mindful that we want to avoid confusion with people looking for EV charger Stations to drive and plug in their cars. We are a contractor not a place to plug in! The name may be problematic in this sense.
Looking for a site that coordinates style & color with the provided VoltNest logo. Would like to have a contact / inquiry page with a captcha or similar tool to weed out spam. need to integrate google maps and similar tools to measure marketing, assist in lead generation, etc.
Have Logo artwork. Not sure what format is best to upload.

Target Market(s)

People with electric cars, business owners and homeowners.

Industry/Entity Type

Electrical Contractor- Residential & Light Commercial (mostly residential)

Coding

Coded - Design and coding required

Number of Pages Required

3 page

Requirements
Must have
• Landing Page/about us , Contact Us/ inquiry Page with a quality captcha filter, Job Gallery- we don't have many pics yet. Google pointers /tools. Open to suggestions here! Mobile Phone/ Tablet friendly is important. I listed coded design but not quite sure what that means.
Nice to have
• Similar to the Brannock Electric site style a possibility, but open to suggestions. Possibly have something that shows the business is connected to Brannock Electric? ..."A division of Brannock Electric" with logo/link to site?

```html
<!DOCTYPE html>
<html lang="en">
<head>
<meta charset="utf-8">
<title>VoltNest EV Charger Installation</title>
<link href="https://fonts.googleapis.com/css2?family=Krona+One&family=Roboto:wght@300;400;500;700&display=swap" rel="stylesheet">
<style>
:root{
  --green:#8dc63f;
  --green-dark:#79b22c;
  --ink:#111111;
  --dark:#1b1b1b;
  --white:#ffffff;
  --text:#222222;
  --muted:#cfcfcf;
}
*{margin:0;padding:0;box-sizing:border-box}
html,body{width:1200px;height:3257px;overflow:hidden}
body{position:relative;background:var(--white);font-family:"Roboto",sans-serif;color:var(--text)}
.abs{position:absolute}
.display{font-family:"Krona One",sans-serif;text-transform:uppercase;letter-spacing:1px}
.accent{color:var(--green)}
.btn{position:absolute;display:flex;align-items:center;justify-content:center;background:var(--green);color:var(--white);border-radius:30px;font-family:"Krona One",sans-serif;text-transform:uppercase;text-decoration:none;letter-spacing:1px}

/* header */
.site-header{position:absolute;left:0;top:0;width:1200px;height:104px;background:var(--white)}
.brand{position:absolute;left:152px;top:20px;display:flex;align-items:center;gap:12px}
.brand-dot{width:34px;height:34px;border-radius:50%;background:var(--green)}
.brand-name{font-family:"Krona One",sans-serif;font-size:30px;color:var(--ink)}
.brand-tag{position:absolute;left:198px;top:66px;font-size:10px;font-weight:500;letter-spacing:.5px;color:var(--ink)}
.header-phone{position:absolute;left:649px;top:14px;display:flex;align-items:center;gap:10px;font-family:"Krona One",sans-serif;font-size:16px;color:var(--ink)}
.phone-icon{width:28px;height:28px;border-radius:50%;background:var(--green);display:flex;align-items:center;justify-content:center}
.header-quote{left:894px;top:11px;width:157px;height:40px;font-size:12px}
.main-nav a{position:absolute;top:67px;font-family:"Krona One",sans-serif;font-size:12px;color:var(--ink);text-decoration:none}

/* hero */
.hero{position:absolute;left:0;top:104px;width:1200px;height:526px;background:linear-gradient(100deg,#cfc7b2 0%,#b9ae94 30%,#9a9b98 55%,#c7cbd0 80%,#8e9094 100%)}
.hero-shade{position:absolute;inset:0;background:rgba(0,0,0,.18)}
.hero-title{position:absolute;left:0;top:158px;width:1200px;text-align:center;font-size:58px;color:var(--white)}
.hero-sub{position:absolute;left:0;top:237px;width:1200px;text-align:center;font-size:34px;font-weight:300;color:var(--white)}
.hero-cta{left:484px;top:303px;width:232px;height:47px;font-size:16px}

/* about */
.about-photo{position:absolute;left:152px;top:725px;width:406px;height:368px;border-radius:200px 0 0 200px;background:linear-gradient(135deg,#d9c7a6,#c4ad86 55%,#e8e6e1)}
.section-title{font-family:"Krona One",sans-serif;text-transform:uppercase;color:var(--ink)}
.about-title{position:absolute;left:637px;top:712px;font-size:38px}
.about-copy{position:absolute;left:637px;top:786px;width:418px;font-size:13.2px;line-height:19.4px;color:var(--text)}
.about-cta{left:637px;top:1042px;width:190px;height:48px;font-size:15px}

/* services */
.services{position:absolute;left:0;top:1190px;width:1200px;height:458px;overflow:hidden}
.services svg{position:absolute;inset:0}
.service{position:absolute;top:0;width:420px;text-align:center}
.service-icon{position:absolute;left:147px;top:96px;width:126px;height:126px;border-radius:50%;display:flex;align-items:center;justify-content:center}
.service-title{position:absolute;left:-20px;top:244px;width:460px;font-size:20px;color:var(--white)}
.service-text{position:absolute;left:20px;top:279px;width:380px;font-size:14px;line-height:17px;color:var(--white)}
.service-link{position:absolute;left:0;top:347px;width:420px;font-family:"Krona One",sans-serif;font-size:13px;text-transform:uppercase;text-decoration:underline}

/* gallery */
.gallery-title{position:absolute;left:0;top:1728px;width:1200px;text-align:center;font-size:40px}
.gallery-item{position:absolute;top:1812px;height:259px;width:213px}
.gallery-cta{left:517px;top:2117px;width:166px;height:48px;font-size:15px}

/* contact */
.map{position:absolute;left:0;top:2251px;width:1200px;height:522px;background:linear-gradient(90deg,#9fcf5e 0%,#a9d46c 35%,#dcdcd4 40%,#e6e4de 75%,#e3ddd0 100%)}
.contact-card{position:absolute;left:152px;top:2330px;width:393px;height:395px;background:var(--white)}
.contact-title{position:absolute;left:43px;top:52px;font-size:26px}
.contact-item{position:absolute;left:43px;display:flex;gap:16px}
.contact-icon{flex:none;width:34px;height:34px;border-radius:50%;background:var(--green);display:flex;align-items:center;justify-content:center}
.contact-item h3{font-size:22px;font-weight:500;color:var(--ink)}
.contact-item p{font-size:18px;line-height:22px;color:var(--text);margin-top:6px}
.map-pin{position:absolute;left:808px;top:2365px}
.map-label{position:absolute;left:733px;top:2428px;width:205px;height:86px;background:var(--white);box-shadow:0 2px 6px rgba(0,0,0,.25);padding:22px 12px 0 12px;font-size:17.5px;line-height:22px;color:var(--ink)}

/* footer */
.site-footer{position:absolute;left:0;top:2773px;width:1200px;height:484px;background:var(--dark)}
.footer-brand{position:absolute;left:152px;top:72px;display:flex;align-items:center;gap:12px}
.footer-brand .brand-dot{width:30px;height:30px}
.footer-brand .brand-name{color:var(--white);font-size:28px}
.footer-copy{position:absolute;left:169px;width:500px;font-size:14.5px;line-height:21px;color:var(--white)}
.partner-name{position:absolute;left:172px;top:222px;font-family:"Krona One",sans-serif;font-size:26px;color:var(--white);text-transform:uppercase}
.social{position:absolute;top:371px;width:32px;height:32px;border-radius:50%;border:2px solid var(--green)}
.copyright{position:absolute;left:150px;top:438px;font-size:11px;color:var(--white)}
.quote-form{position:absolute;left:716px;top:61px;width:339px;height:350px;background:var(--green)}
.quote-form h2{position:absolute;left:30px;top:30px;font-size:16px;color:var(--ink)}
.field{position:absolute;left:30px;width:283px;border-bottom:1px solid var(--ink);font-size:13px;color:var(--ink)}
.submit{position:absolute;left:31px;top:274px;width:125px;height:44px;border-radius:25px;background:var(--ink);color:var(--white);font-family:"Krona One",sans-serif;font-size:13px;display:flex;align-items:center;justify-content:center;text-transform:uppercase}
</style>
</head>
<body>

<header class="site-header">
  <div class="brand"><span class="brand-dot"></span><span class="brand-name">VoltNest</span></div>
  <div class="brand-tag">EV CHARGER INSTALLATION</div>
  <div class="header-phone">
    <span class="phone-icon"><svg width="16" height="16" viewBox="0 0 24 24"><path fill="#fff" d="M6.6 10.8a15.1 15.1 0 0 0 6.6 6.6l2.2-2.2a1 1 0 0 1 1-.25 11.4 11.4 0 0 0 3.6.57 1 1 0 0 1 1 1V20a1 1 0 0 1-1 1A17 17 0 0 1 3 4a1 1 0 0 1 1-1h3.5a1 1 0 0 1 1 1c0 1.25.2 2.45.57 3.57a1 1 0 0 1-.25 1z"/></svg></span>
    888 888 8888
  </div>
  <a class="btn header-quote" href="#quote">Get a Quote</a>
  <nav class="main-nav">
    <a href="#" style="left:597px">Home</a>
    <a href="#about" style="left:687px">About Us</a>
    <a href="#services" style="left:816px">Services</a>
    <a href="#contact" style="left:942px">Contact Us</a>
  </nav>
</header>

<section class="hero" role="img" aria-label="Photo of a wall-mounted EV charger in a garage beside a parked electric truck">
  <div class="hero-shade"></div>
  <h1 class="hero-title display">VoltNest</h1>
  <p class="hero-sub">EV CHARGER INSTALLATION</p>
  <a class="btn hero-cta" href="#quote">Get a Quote</a>
</section>

<section id="about">
  <div class="about-photo" role="img" aria-label="Photo of electrical panels and a home battery mounted on a plywood wall"></div>
  <h2 class="section-title about-title">About <span class="accent">Us</span></h2>
  <p class="about-copy">EV charger installation is a relatively simple process, but it's important to hire a qualified electrician. VoltNest is a division of Brannock Electric, a licensed and insured electrical contractor. We are committed to providing our customers with a quality, code approved installation. We'll assess your home's electrical system and help find a safe and convenient location for the charger or charger outlet.In some cases, a homeor business electrical panel or Main electrical service system may require an upgrade to accommodate adding an EV charger(s). Additionally, some jurisdictions require that a home's smoke detectors be brought up to current code standards. We can help you determine if any upgrades are necessary and can provide you with a quote for the work.</p>
  <a class="btn about-cta" href="#">Read More</a>
</section>

<section class="services" id="services">
  <svg width="1200" height="458" viewBox="0 0 1200 458">
    <rect width="1200" height="458" fill="#2a2724"/>
    <polygon points="556,0 1200,0 1200,458 639,458" fill="#8dc63f"/>
    <polygon points="556,0 1200,0 1200,458 639,458" fill="#a5d35f" opacity=".25"/>
  </svg>
  <div role="img" aria-label="Photo of an outdoor meter box on a wooden post" style="position:absolute;left:0;top:0;width:600px;height:458px"></div>
  <div class="service" style="left:134px">
    <div class="service-icon" style="background:var(--green);border:5px solid var(--ink)">
      <svg width="64" height="64" viewBox="0 0 64 64" fill="#111"><rect x="10" y="8" width="22" height="50"/><rect x="32" y="22" width="22" height="36"/><g fill="#8dc63f"><rect x="14" y="14" width="5" height="5"/><rect x="23" y="14" width="5" height="5"/><rect x="14" y="24" width="5" height="5"/><rect x="23" y="24" width="5" height="5"/><rect x="14" y="34" width="5" height="5"/><rect x="23" y="34" width="5" height="5"/><rect x="37" y="28" width="5" height="5"/><rect x="45" y="28" width="5" height="5"/><rect x="37" y="38" width="5" height="5"/><rect x="45" y="38" width="5" height="5"/></g></svg>
    </div>
    <h3 class="service-title display">Commercial Service</h3>
    <p class="service-text">Lorem ipsum dolor sit amet, consectetur adipiscing elit, sed do eiusmod tempor incididunt ut labore et dolore magna aliqua.</p>
    <a class="service-link" href="#" style="color:var(--green)">Read More</a>
  </div>
  <div class="service" style="left:635px">
    <div class="service-icon" style="background:var(--ink)">
      <svg width="70" height="64" viewBox="0 0 70 64" fill="none" stroke="#8dc63f" stroke-width="4"><path d="M6 30 35 6l29 24"/><path d="M14 24v32h42V24"/><rect x="22" y="36" width="10" height="20"/><rect x="38" y="34" width="12" height="10"/><path d="M6 58h58"/></svg>
    </div>
    <h3 class="service-title display">Residential Service</h3>
    <p class="service-text">Lorem ipsum dolor sit amet, consectetur adipiscing elit, sed do eiusmod tempor incididunt ut labore et dolore magna aliqua.</p>
    <a class="service-link" href="#" style="color:var(--ink)">Read More</a>
  </div>
</section>

<section id="gallery">
  <h2 class="section-title gallery-title">Our <span class="accent">Gallery</span></h2>
  <div class="gallery-item" style="left:150px;background:linear-gradient(#e9e3d6,#cfc6b4)" role="img" aria-label="Photo of a wall-mounted EV charger with coiled cable"></div>
  <div class="gallery-item" style="left:381px;background:linear-gradient(120deg,#4d6a3c,#b98b5a 45%,#8a6440)" role="img" aria-label="Photo of an outdoor meter mounted on a wooden post"></div>
  <div class="gallery-item" style="left:609px;background:linear-gradient(90deg,#cfcac2,#3a3632 45%,#d8d4cc)" role="img" aria-label="Photo of an open breaker panel with wiring"></div>
  <div class="gallery-item" style="left:838px;background:linear-gradient(90deg,#c9c7c2,#7d7f80 50%,#e8e6e2)" role="img" aria-label="Photo of service panels and a meter on a garage wall"></div>
  <a class="btn gallery-cta" href="#">View All</a>
</section>

<section id="contact">
  <div class="map" role="img" aria-label="Street map around the business location"></div>
  <div class="contact-card">
    <h2 class="section-title contact-title">Contact <span class="accent">Us</span></h2>
    <div class="contact-item" style="top:114px">
      <span class="contact-icon"><svg width="14" height="18" viewBox="0 0 14 18"><path fill="#fff" d="M7 0a7 7 0 0 0-7 7c0 5 7 11 7 11s7-6 7-11a7 7 0 0 0-7-7zm0 9.5A2.5 2.5 0 1 1 7 4.5a2.5 2.5 0 0 1 0 5z"/></svg></span>
      <div><h3>Location</h3><p>123 ipsum dolor sit amet, coect<br>etur st.no 12/3</p></div>
    </div>
    <div class="contact-item" style="top:207px">
      <span class="contact-icon"><svg width="16" height="16" viewBox="0 0 24 24"><path fill="#fff" d="M6.6 10.8a15.1 15.1 0 0 0 6.6 6.6l2.2-2.2a1 1 0 0 1 1-.25 11.4 11.4 0 0 0 3.6.57 1 1 0 0 1 1 1V20a1 1 0 0 1-1 1A17 17 0 0 1 3 4a1 1 0 0 1 1-1h3.5a1 1 0 0 1 1 1c0 1.25.2 2.45.57 3.57a1 1 0 0 1-.25 1z"/></svg></span>
      <div><h3>Call Us</h3><p>888 888 8888</p></div>
    </div>
    <div class="contact-item" style="top:279px">
      <span class="contact-icon"><svg width="18" height="14" viewBox="0 0 18 14"><rect x="1" y="1" width="16" height="12" rx="1" fill="none" stroke="#fff" stroke-width="2"/><path d="M1 2l8 6 8-6" fill="none" stroke="#fff" stroke-width="2"/></svg></span>
      <div><h3>Email Us</h3><p>info@voltnestelectric.example</p></div>
    </div>
  </div>
  <svg class="map-pin" width="46" height="58" viewBox="0 0 46 58"><path d="M23 0A23 23 0 0 0 0 23c0 16 23 35 23 35s23-19 23-35A23 23 0 0 0 23 0z" fill="#e0282a"/><circle cx="23" cy="22" r="8" fill="#fff"/></svg>
  <div class="map-label">123ipsum dolor amet, consecteturst.no 134</div>
</section>

<footer class="site-footer">
  <div class="footer-brand"><span class="brand-dot"></span><span class="brand-name">VoltNest</span></div>
  <p class="footer-copy" style="top:159px">Lorem ipsum dolor sit amet, consectetur adipiscing elit, sed do eiusmod tempor incididunt ut labore et dolore magna aliqua.</p>
  <div class="partner-name">Brannock Electric</div>
  <p class="footer-copy" style="top:305px">Lorem ipsum dolor sit amet, consectetur adipiscing elit, sed do eiusmod tempor incididunt ut labore et dolore magna aliqua.</p>
  <span class="social" style="left:151px"></span>
  <span class="social" style="left:198px"></span>
  <span class="social" style="left:234px"></span>
  <p class="copyright">© COPYRIGHT 2023 VOLTNEST EV CHARGER INSTALLATION</p>

  <form class="quote-form" id="quote">
    <h2 class="display">Get a Quote</h2>
    <div class="field" style="top:68px;height:24px">Name</div>
    <div class="field" style="top:114px;height:25px">Email Address</div>
    <div class="field" style="top:161px;height:25px">Phone Number</div>
    <div class="field" style="top:207px;height:47px">Message</div>
    <div class="submit">Submit</div>
  </form>
</footer>

</body>
</html>
```